QVB Commercial Roof Restoration LLC needs billboard and banner designs

Need billboard ad design for small commercial roof restoration company. Looking for a billboard design that can be used on digital and hard print billboards. Also need banner design for 4' x 8' job site banners that will go by roadside to draw potential customers to our brand. Our vision for bill board would show an attractive women in business dress, clearly in a building having to use an (red) umbrella (inside building) due to leaking roof. Caption "WE CAN HELP" www.QVBCOMMERCIALROOF.example
For banner design we would use some before/after roof photos (attached, blend/overlay at an angle) in background with "Another Quality Commercial Roof Restoration By:" "QVB Commercial Roof LLC" "Is your commercial roof leaking? Call 555.314.0827 for help".
All final designs should communicate commercial roof restoration only.
Target Market(s)
Commercial building owner/managers
Industry/Entity Type
Roofing
Requirements
Must have
- Just added a Jpeg file of a logo of the company that we buy our products from. This logo & "Certified Premier Installers" needs to be added to the project. It only needs to have a small footprint on the ad. Contact me if you have questions. Thank you.
Nice to have
- Billboard design; our name, website, relay our message with image. As described above in project description
Banner; Our name, phone number and bold written message

```html
<!DOCTYPE html>
<html lang="en">
<head>
<meta charset="utf-8">
<title>QVB Commercial Roof Restoration – Billboard</title>
<link rel="stylesheet" href="https://fonts.googleapis.com/css2?family=Source+Sans+3:wght@700;800&display=swap">
<style>
  :root {
    --page: #ffffff;
    --paper: #f1f0ee;
    --roof-light: #f6f5f3;
    --roof-mid: #e2dfda;
    --red: #c4261d;
    --blue: #0b4c9c;
    --ink: #3c3c3c;
    --white: #ffffff;
    --photo-warm: #c9a877;
    --photo-light: #ece6dc;
    --photo-red: #d9231c;
  }
  html, body {
    margin: 0;
    width: 1200px;
    height: 1200px;
    overflow: hidden;
    background: var(--page);
    font-family: "Source Sans 3", "Myriad Pro", Arial, sans-serif;
  }
  .billboard {
    position: absolute;
    left: 50px;
    top: 325px;
    width: 1100px;
    height: 550px;
    overflow: hidden;
    background: var(--paper);
    box-shadow: 0 6px 18px rgba(0,0,0,.25);
  }
  .billboard__backdrop {
    position: absolute;
    inset: 0;
    background: linear-gradient(160deg, var(--roof-light) 0%, var(--roof-mid) 55%, var(--roof-light) 100%);
  }
  .brand {
    position: absolute;
    left: 42px;
    top: 34px;
    display: flex;
    flex-direction: column;
    color: var(--blue);
    font-weight: 800;
    line-height: 1;
  }
  .brand__name { font-size: 56px; letter-spacing: 4px; }
  .brand__line { font-size: 18px; margin-top: 4px; }
  .headline {
    position: absolute;
    left: 40px;
    top: 138px;
    margin: 0;
    font-weight: 700;
    line-height: .9;
    text-transform: uppercase;
  }
  .headline span { display: block; }
  .headline__top { color: var(--red); font-size: 87px; }
  .headline__middle { color: var(--blue); font-size: 59px; margin-top: 4px; }
  .headline__bottom { color: var(--red); font-size: 111px; letter-spacing: -1px; margin-top: -4px; }
  .cta-band {
    position: absolute;
    left: 0;
    top: 384px;
    width: 760px;
    height: 84px;
    background: var(--blue);
  }
  .cta-band__text {
    position: absolute;
    left: 42px;
    top: 2px;
    margin: 0;
    color: var(--white);
    font-size: 76px;
    font-weight: 700;
    line-height: 84px;
  }
  .web-address {
    position: absolute;
    left: 42px;
    top: 483px;
    margin: 0;
    color: var(--ink);
    font-size: 37px;
    font-weight: 700;
  }
  .hero {
    position: absolute;
    inset: 0;
    width: 1100px;
    height: 550px;
  }
</style>
</head>
<body>
  <main class="billboard">
    <div class="billboard__backdrop" role="img" aria-label="Faint photo of a commercial metal roof surface"></div>

    <div class="brand" aria-label="QVB Commercial Roof Restoration">
      <span class="brand__name">QVB</span>
      <span class="brand__line">COMMERCIAL</span>
      <span class="brand__line">ROOF RESTORATION</span>
    </div>

    <h1 class="headline">
      <span class="headline__top">Commercial</span>
      <span class="headline__middle">Roof Restoration</span>
      <span class="headline__bottom">Company</span>
    </h1>

    <div class="cta-band">
      <p class="cta-band__text">WE CAN HELP</p>
    </div>

    <p class="web-address">www.QVBCOMMERCIALROOF.example</p>

    <svg class="hero" viewBox="0 0 1100 550" aria-hidden="false">
      <defs>
        <linearGradient id="heroTone" x1="0" y1="0" x2="1" y2="1">
          <stop offset="0" stop-color="var(--photo-warm)"/>
          <stop offset=".45" stop-color="var(--photo-light)"/>
          <stop offset=".75" stop-color="var(--photo-red)"/>
          <stop offset="1" stop-color="#2b2b2b"/>
        </linearGradient>
      </defs>
      <path d="M832 0 C760 60 706 170 700 300 C696 400 712 480 742 550" fill="none" stroke="var(--blue)" stroke-width="8"/>
      <path d="M848 0 C776 62 722 172 716 300 C712 400 728 480 758 550" fill="none" stroke="var(--red)" stroke-width="6"/>
      <path role="img" aria-label="Photo of a businesswoman holding a red umbrella indoors under a collapsed, leaking ceiling"
            d="M864 0 L1100 0 L1100 550 L774 550 C744 480 728 400 732 300 C738 172 792 62 864 0 Z"
            fill="url(#heroTone)"/>
    </svg>
  </main>
</body>
</html>
```